Corporate Capability Statement for Brenwick Procurement Partners LLC

Create Corporate Capability Statement for Consulting Firm small business start-up. Minority woman-owned consulting firm based in Washington, DC metropolitan area with a target market of the local and federal government. Would like see some area government images such as buildings or monuments. Sending previous Cape Statement which really need a complete over haul. Looking for something eye-catching and creates a strong presence. The final design should communicate our numerous service offerings.

Target Market(s)

Government

Industry/Entity Type

Management Consulting

Font styles to use
Serif
Sans Serif

Requirements
Must have
• Must be able to showcase all service offerings on one-page. Usage of company colors blue and gray.
Nice to have
• images of Washington DC or government monuments illustrated in the document.
• Nice to have my contact info listed on the cape statement somewhere with the updated info below:
• Company POC: Marisol T. Fenwick, CEO & Founder
• Ridgemont, MD 20999 | 202.571.3346 | info@brenwickpartners-example.com | www.brenwickpartners-example.com

```html
<!DOCTYPE html>
<html lang="en">
<head>
<meta charset="utf-8">
<title>Brenwick Procurement Partners – Capabilities Statement</title>
<link href="https://fonts.googleapis.com/css2?family=Bebas+Neue&family=Oswald:wght@500;600&family=Lato:wght@400;700&display=swap" rel="stylesheet">
<style>
:root{
  --blue:#0a55a8;
  --blue-dark:#06428a;
  --ink:#222;
  --grey-line:#8a8a8a;
  --grey-cell:#e6e6e6;
  --grey-head:#efefef;
  --bg:#ffffff;
}
*{box-sizing:border-box;margin:0;padding:0}
html,body{width:1200px;height:1200px;overflow:hidden;background:var(--bg)}
body{font-family:"Lato",sans-serif;color:var(--ink)}
.page{position:absolute;left:176px;top:0;width:848px;height:1200px;background:#fff;overflow:hidden}
.abs{position:absolute}
.header{left:0;top:0;width:848px;height:272px;background:linear-gradient(#fafafa,#e4e4e4)}
.top-band{left:0;top:0;width:848px;height:29px;background:var(--blue)}
.title-block{left:0;top:0}
.doc-title{left:650px;top:24px;width:185px;font-family:"Bebas Neue",sans-serif;font-size:40px;line-height:38px;color:#fff;text-align:center}
.section-title{font-size:17px;color:var(--blue);letter-spacing:.2px}
.body-copy{font-size:12.6px;line-height:15.4px;text-align:justify}
.overview-title{left:35px;top:44px}
.overview-copy{left:35px;top:82px;width:373px}
.why-title{left:460px;top:104px}
.why-copy{left:460px;top:140px;width:351px}
.brand{left:40px;top:330px;width:138px;text-align:center}
.brand-mark{width:14px;height:14px;background:var(--blue);margin:0 auto 8px}
.brand-name{font-size:22px;font-weight:700;letter-spacing:3px;color:var(--blue-dark)}
.photo{top:284px;height:129px;border:3px solid #c8c8c8}
.photo-1{left:202px;width:190px;background:linear-gradient(#8fb8e6 0%,#dfe8f0 45%,#f4f4f4 60%,#5f7d45 100%)}
.photo-2{left:412px;width:189px;background:linear-gradient(#3f86d6 0%,#9cc4ee 40%,#e3e3de 65%,#6f8f4a 100%)}
.photo-3{left:621px;width:190px;background:linear-gradient(#3c7bd0 0%,#8bb6e6 35%,#e6e4dc 60%,#c9c6bc 100%)}
.bar{background:var(--blue);color:#fff;font-family:"Oswald",sans-serif;font-weight:500;font-size:11.5px;padding-left:10px;display:flex;align-items:center;height:23px}
.offer-bar{left:35px;top:428px;width:191px;height:25px;font-family:"Bebas Neue",sans-serif;font-size:19px;padding-left:4px}
.offers{left:35px;top:456px;width:777px;border:1px solid var(--grey-line)}
.offer{display:grid;grid-template-columns:102px 1fr;border-top:1px solid var(--grey-line)}
.offer:first-child{border-top:0}
.offer-label{font-family:"Bebas Neue",sans-serif;font-size:17px;line-height:15.5px;color:var(--blue);text-align:center;display:flex;align-items:center;justify-content:center;border-right:1px solid var(--grey-line)}
.offer-text{font-size:12.4px;line-height:15.4px;text-align:justify;padding:7px 8px 0 7px}
.info-table{border:1px solid var(--grey-line);border-top:0}
.info-row{display:grid;border-top:1px solid var(--grey-line);background:linear-gradient(#f6f6f6,#e2e2e2);font-size:12.6px;line-height:15.4px}
.info-row>div{padding:4px 12px}
.info-row>div:first-child{border-right:1px solid var(--grey-line)}
.contact .info-row,.general .info-row{grid-template-columns:112px 1fr}
.naics .info-row{grid-template-columns:98px 1fr}
.contact-bar{left:35px;top:804px;width:376px;height:25px}
.contact{left:35px;top:829px;width:376px}
.general-bar{left:35px;top:923px;width:376px;height:21px}
.general{left:35px;top:944px;width:376px}
.naics-bar{left:436px;top:804px;width:376px;height:25px}
.naics{left:436px;top:829px;width:376px}
.sic-bar{left:35px;top:1118px;width:376px;height:21px}
.sic-box{left:35px;top:1143px;width:376px;height:32px}
.psc-bar{left:436px;top:1118px;width:376px;height:21px}
.psc-box{left:436px;top:1143px;width:376px;height:32px}
.small-box{border:1px solid var(--grey-line);background:linear-gradient(#f6f6f6,#e2e2e2);font-size:10.8px;line-height:13.5px;padding:2px 6px}
.bottom-band{left:0;top:1184px;width:848px;height:16px;background:var(--blue)}
</style>
</head>
<body>
<div class="page">
  <div class="abs header"></div>
  <div class="abs top-band"></div>
  <svg class="abs title-block" width="848" height="120" viewBox="0 0 848 120" aria-hidden="true">
    <polygon points="571,29 848,29 848,112 612,112" fill="#0a55a8"/>
  </svg>
  <div class="abs doc-title">Capabilities Statement</div>

  <h2 class="abs section-title overview-title">COMPANY OVERVIEW</h2>
  <p class="abs body-copy overview-copy">Brenwick Procurement Partners (BPP), LLC is a woman-owned management consulting firm which provides a full suite of professional services and cutting edge solutions for government and private sector clients. We are process driven and results focused with the highest standards of ethics and integrity in all aspects of our business model. BPP’s consultants possess a significant degree of expertise and industry experience with a proven track record of providing professional excellence to our private sector and government clientele. We are dedicated to exceeding our clients’ expectations through lifecycle project management that incorporates institutional knowledge and industry best practices that will ensure the highest possible quality of end product delivery.</p>

  <h2 class="abs section-title why-title">WHY CHOOSE US</h2>
  <p class="abs body-copy why-copy">BPP’s executive management team and consultants have a proven track record of over 50+ years’ experience in providing professional consulting services to meet our client’s specific business needs. Our extensive expertise in working alongside some of the industry’s top professionals has gained us a unique competitive edge which enables us to assist our customers… Leading them to new relationships and concrete opportunities for growth and success.</p>

  <div class="abs brand">
    <div class="brand-mark"></div>
    <div class="brand-name">BRENWICK</div>
  </div>
  <div class="abs photo photo-1" role="img" aria-label="Photo of the White House north portico with fountain and trees"></div>
  <div class="abs photo photo-2" role="img" aria-label="Photo of the U.S. Capitol dome against a blue sky"></div>
  <div class="abs photo photo-3" role="img" aria-label="Photo of the U.S. Capitol building facade and dome"></div>

  <div class="abs bar offer-bar">Business Service Offerings</div>
  <div class="abs offers">
    <div class="offer" style="height:46px"><div class="offer-label">Acquisition<br>Management</div><div class="offer-text">Advisory, Acquisition Planning &amp; Strategy, Contract Cost Estimating &amp; Pricing, Contract Negotiation, Pre &amp; Post Award Contract Administration, Procurement Package Development and Contract Closeout Support.</div></div>
    <div class="offer" style="height:60px"><div class="offer-label">Administrative<br>Support</div><div class="offer-text">Professional staffing support to government, public, private, and non-profit organizations providing outsourced confidential administrative and financial staff augmentation, bookkeeping, program &amp; project support, marketing and sales assistance as well as other related services.</div></div>
    <div class="offer" style="height:49px"><div class="offer-label">Business<br>Development</div><div class="offer-text">Business Branding, Capture Management, Document Compilation Support, Market Research &amp; Analysis, Proposal Development &amp; Management, Prospecting &amp; Lead Generation and Small Business Commercialization.</div></div>
    <div class="offer" style="height:60px"><div class="offer-label">Legal<br>Services</div><div class="offer-text">BPP also provides legal counsel offerings providing a broad range of disciplines and projects. Offerings to include; Contract Business Law, Policy Advisory, FAR/DFAR Regulations, Collections Practice, Civil Litigation Support, Dispute Resolution, and Employment Law services.</div></div>
    <div class="offer" style="height:48px"><div class="offer-label">Process<br>Improvement</div><div class="offer-text">Business Process Mapping &amp; Re-engineering, Change &amp; Transition Management, Quality Assurance, Risk Management &amp; Surveillance and Standard Operating Procedures, Strategic Policy &amp; Governance, Technical Writing Support.</div></div>
    <div class="offer" style="height:75px"><div class="offer-label">Program<br>Management</div><div class="offer-text">Administrative Services, Federal Accounting Compliance &amp; Standards, Government Financial System Transactions &amp; Management Support, Factsheets, Technical &amp; Fiscal Business Cases, Performance Measurement, Government Infrastructure Functional Support and Independent Verification &amp; Validation (IV&amp;V), OMB Circulars and OMB Scorecard Results reporting.</div></div>
  </div>

  <div class="abs bar contact-bar">COMPANY CONTACT</div>
  <div class="abs info-table contact">
    <div class="info-row" style="height:39px"><div>ADDRESS:</div><div>48 Harrow Crest Lane<br>Ridgemont, MD 20999</div></div>
    <div class="info-row" style="height:25px"><div>PHONE:</div><div>(202) 571-3346</div></div>
    <div class="info-row" style="height:26px"><div>EMAIL:</div><div style="font-size:11.6px">mfenwick@brenwickpartners-example.com</div></div>
  </div>

  <div class="abs bar general-bar">GENERAL INFORMATION</div>
  <div class="abs info-table general">
    <div class="info-row" style="height:31px"><div style="padding-top:11px">EIN:</div><div style="padding-top:6px">58-3129065</div></div>
    <div class="info-row" style="height:27px"><div>DUNS:</div><div style="padding-top:6px">091847352</div></div>
    <div class="info-row" style="height:28px"><div style="padding-top:7px">CAGE CODE:</div><div style="padding-top:7px">7KRP2</div></div>
    <div class="info-row" style="height:56px"><div style="padding-top:7px">SET-ASIDE:</div><div>Economically Disadvantaged Woman-Owned Small Business (EDWOSB) – SBA Registered</div></div>
    <div class="info-row" style="height:28px"><div style="padding-top:6px">Sole Source</div><div style="padding-top:6px">WOSB/EDWOSB</div></div>
  </div>

  <div class="abs bar naics-bar">NAICS CODES</div>
  <div class="abs info-table naics">
    <div class="info-row" style="height:28px"><div style="padding-top:6px">541210</div><div style="padding-top:6px">Data Analysis and Compilation</div></div>
    <div class="info-row" style="height:26px"><div>541110</div><div>Offices of Lawyers</div></div>
    <div class="info-row" style="height:55px"><div>541611</div><div style="text-align:justify">Administrative Management and General Management Consulting Services,Strategic Planning; Small Business Start-up’s</div></div>
    <div class="info-row" style="height:33px"><div style="padding-top:9px">541613</div><div style="padding-top:7px">Marketing Consulting Services</div></div>
    <div class="info-row" style="height:32px"><div style="padding-top:8px">541618</div><div style="padding-top:5px">Other Management Consulting Services</div></div>
    <div class="info-row" style="height:43px"><div style="padding-top:15px">541990</div><div>All other Professional,Scientific,and Technical Services; Policy &amp; Procedure Writing</div></div>
    <div class="info-row" style="height:36px"><div style="padding-top:12px">541990</div><div style="padding-top:9px">Document Preparation Services</div></div>
    <div class="info-row" style="height:32px"><div style="padding-top:8px">561499</div><div style="padding-top:8px">All other Business Support Services</div></div>
  </div>

  <div class="abs bar sic-bar">SIC CODE</div>
  <div class="abs small-box sic-box">8111 – Legal Services<br>8742 – Management Consulting Services</div>

  <div class="abs bar psc-bar">PSC CODES</div>
  <div class="abs small-box psc-box">R406, &nbsp;R408, &nbsp;R410, &nbsp;R418, &nbsp;R499, &nbsp;R704, &nbsp;R707,<br>R799</div>

  <div class="abs bottom-band"></div>
</div>
</body>
</html>
```